We are looking for a new website design for our SEO WEB Development Company. The URL is www.brellowcreativeworks.com

We want it to be a more powerful representation of what we do. We are also looking for a number of designers that we will give continuous business to every month. The persons design we choose will also get a proposal to complete 4 - 6 new designs for us every month for our clients.

Be creative as you can in your design submissions. We really want to stand out!

Just to give you an idea of what we like look at this site: http://www.tovandigitalstudio.com/

```html
<!DOCTYPE html>
<html lang="en">
<head>
<meta charset="utf-8">
<title>Brellow Interactive Group</title>
<link href="https://fonts.googleapis.com/css2?family=Arimo:wght@400;700&family=Oswald:wght@400;500&family=Roboto+Condensed:wght@400;700&display=swap" rel="stylesheet">
<style>
:root{
  --orange:#e07a10;
  --brown-dark:#2e2620;
  --brown-mid:#3f352d;
  --beige:#ece3d7;
  --beige-deep:#d9cbb8;
  --text:#3a3530;
  --muted:#9d9084;
  --side-text:#b3a699;
  --green-top:#a9cf5b;
  --green-bot:#7fae2e;
  --white:#ffffff;
}
*{margin:0;padding:0;box-sizing:border-box}
html,body{width:900px;height:1200px;overflow:hidden}
body{font-family:"Arimo",Arial,sans-serif;color:var(--text);background:var(--white);position:relative}
.top-band{position:absolute;left:0;top:0;width:900px;height:420px;background:linear-gradient(#f3eee8 0,#e8dfd3 110px,#d8cbbb 300px,#f4f0eb 420px)}
.header{position:absolute;left:0;top:0;width:900px;height:100px}
.brand{position:absolute;left:96px;top:14px;display:flex;align-items:center;gap:10px}
.brand-mark{width:16px;height:16px;background:var(--orange)}
.brand-name{font-family:"Arimo",Arial,sans-serif;font-weight:700;font-size:34px;color:var(--orange);line-height:1}
.brand-sub{position:absolute;left:96px;top:56px;font-size:13px;letter-spacing:1px;color:#6d5f52}
.quote-call{position:absolute;right:100px;top:6px;text-align:right}
.quote-call .label{font-size:15px;color:#4a4039}
.quote-call .phone{font-size:16px;font-weight:700;color:var(--orange);margin-top:4px}
.nav{position:absolute;right:96px;top:58px;display:flex;gap:6px}
.nav a{font-family:"Roboto Condensed",Arial,sans-serif;font-weight:700;font-size:15px;color:#2b241f;text-decoration:none;padding:6px 6px 7px;background:linear-gradient(#fbf8f4,#e3d8ca);border-radius:3px 3px 0 0;white-space:nowrap}
.hero{position:absolute;left:100px;top:120px;width:512px;height:290px;background:var(--white);border:1px solid #e5ddd2;overflow:hidden}
.hero-photo{position:absolute;left:40px;top:0;width:200px;height:234px;background:linear-gradient(#e9e4de,#b9b0a6 60%,#3a3633)}
.hero-copy{position:absolute;right:26px;top:36px;text-align:right}
.hero-title{font-family:"Oswald",Arial,sans-serif;font-weight:500;font-size:25px;line-height:32px;color:var(--orange);white-space:nowrap}
.hero-sub{margin-top:4px;font-family:"Oswald",Arial,sans-serif;font-size:16px;line-height:22px;color:#6f6760;white-space:nowrap}
.hero-bar{position:absolute;left:0;bottom:0;width:100%;height:56px;background:linear-gradient(#eeeae5,#c9c2b9);display:flex;justify-content:space-between;align-items:center;padding:0 22px}
.hero-bar .tag{font-family:"Oswald",Arial,sans-serif;font-size:22px;color:#4a423b;white-space:nowrap}
.hero-bar .call{font-family:"Oswald",Arial,sans-serif;font-size:22px;color:var(--orange);white-space:nowrap}
.quote-form{position:absolute;left:630px;top:120px;width:172px;height:270px;background:linear-gradient(#e7dccd,#d4c4ae);border-radius:4px;padding:12px}
.quote-form h2{font-size:13px;font-weight:400;line-height:17px;color:#2b241f}
.quote-form h2 em{font-style:normal;font-weight:700;color:var(--orange)}
.field{margin-top:8px;height:26px;background:#d9cab7;border:1px solid #cbb9a2;font-size:11px;color:#f4eee7;padding:6px 8px}
.quote-form .field:first-of-type{margin-top:14px}
.submit{margin-top:22px;height:40px;border-radius:4px;background:linear-gradient(var(--green-top),var(--green-bot));color:#243312;font-size:13px;text-align:center;line-height:40px}
.content{position:absolute;left:110px;top:445px;width:492px;font-size:11px;line-height:15px;color:var(--text)}
.content p{margin-bottom:15px}
.sidebar{position:absolute;left:636px;top:443px;width:158px;font-size:11px;line-height:15px;color:var(--side-text)}
.share{position:absolute;left:636px;top:764px;width:164px;height:36px;background:#faf8f6;border:1px solid #eee7df;display:flex;align-items:center;gap:8px;padding:0 10px;font-size:11px;color:#4a423b}
.share-badge{background:#3b5a9a;color:var(--white);font-size:10px;font-weight:700;padding:3px 6px}
.footer{position:absolute;left:0;top:984px;width:900px;height:216px;background:linear-gradient(var(--brown-dark),var(--brown-mid))}
.footer-cols{position:absolute;left:90px;top:22px;display:flex}
.footer-col h3{font-size:12px;font-weight:700;color:var(--white);padding-bottom:12px;border-bottom:1px solid #4c4139;margin-bottom:16px;white-space:nowrap}
.footer-col li{list-style:none;font-size:10px;line-height:15px;color:#8a7d71;white-space:nowrap}
.footer-bottom{position:absolute;left:0;bottom:0;width:100%;height:26px;background:#241e19;display:flex;justify-content:space-between;align-items:center;padding:0 90px;font-size:9px;color:#6d6157}
</style>
</head>
<body>
<div class="top-band"></div>

<header class="header">
  <div class="brand"><span class="brand-mark"></span><span class="brand-name">Brellow</span></div>
  <div class="brand-sub">INTERACTIVE GROUP</div>
  <div class="quote-call">
    <div class="label">Call us for a quote today</div>
    <div class="phone">214-555-0147</div>
  </div>
  <nav class="nav">
    <a href="#">Creative Design</a>
    <a href="#">Website Design</a>
    <a href="#">Internet Marketing</a>
    <a href="#">IT Consulting</a>
  </nav>
</header>

<section class="hero">
  <div class="hero-photo" role="img" aria-label="Businesswoman in a dark suit standing with arms crossed"></div>
  <div class="hero-copy">
    <div class="hero-title">FOCUSING ON YOUR BRAND</div>
    <div class="hero-sub">With the right Internet Marketing tools</div>
  </div>
  <div class="hero-bar">
    <span class="tag">Media Marketing Experts</span>
    <span class="call">Call 877-555-0192</span>
  </div>
</section>

<aside class="quote-form">
  <h2>Get A <em>Free</em> Reputation Management &amp; Repair Quote!</h2>
  <div class="field">Name</div>
  <div class="field">Phone</div>
  <div class="field">Email</div>
  <div class="field">Website</div>
  <div class="submit">Request for Quote</div>
</aside>

<main class="content">
  <p><strong>Brellow Interactive Group</strong> is a leading Dallas Web Site Design, Publishing and Internet Marketing Firm. Our Dallas Texas based Website Design and Internet Marketing experts are some of the best in the industry!</p>
  <p>Brellow Interactive Web is a full-service Dallas based Advertising Agency comprised of experienced advertising and marketing professionals that provide clients with a clear and distinct voice in the marketplace. Web Site Design and Internet Marketing experts at our Dallas location specialize in developing Online Marketing Strategies, Search Engine Marketing and Optimization (SEO), Pay Per Click, Web Site Design and Development, and Online Reputation Management.</p>
  <p>Brellow Interactive Publishing provides full-service custom publishing and consulting services for magazines, newsletters, blogs and web sites. We are the complete interactive publishing arm for your organization. Our services include: Strategic Planning and Computer Modeling; Art Direction and Design; Production Services; Circulation Marketing and Management; Subscription Fulfillment Management; Advertising Sales Management; Web Site and Digital Magazine Design and Management; and Video Streaming Services.</p>
  <p>Brellow Interactive Media provides cost-effective Web Site Design services, Search Engine Marketing, Internet Advertising, Internet Marketing Campaigns and most important, we can accommodate any budget.</p>
  <p>Brellow Interactive Reputation Management and Repair provides reputation management and repair services to the online community. We offer a plan of action to create a process of tracking an entity's actions and other entities' opinions about those actions; reporting on those actions and opinions, and reacting to that report creating a feedback loop. Reputation management has become essential with the advent of widespread computing. Reputation management systems use predefined criteria for processing complex data to report the many factors affecting a company's reputation. However, these systems only facilitate and automate the process of determining trustworthiness.</p>
</main>

<aside class="sidebar">
  The goal of a reputation management or repair campaign is to create and/or strengthen an authoritative, positive image of your company by helping you gain positive name recognition across a wide range of websites. Most Search Engine users only pay attention to the Top 30 results, which is what we focus on. We will work closely with you to come up with a strong, detailed plan to put you at the top of search engines such as Searchly.com and above the negative listings about you. We will analyze your situation closely and create a detailed but flexible plan for your Reputation Management Campaign.
</aside>

<div class="share">Share on <span class="share-badge">Circlepage</span></div>

<footer class="footer">
  <div class="footer-cols">
    <div class="footer-col" style="width:128px"><h3>Creative Design</h3><ul><li>Creative Advertising</li><li>Print Design</li><li>Corporate Identity</li><li>Packaging</li></ul></div>
    <div class="footer-col" style="width:190px"><h3>Internet Marketing Services</h3><ul><li>Search Engine Optimization</li><li>Pay per Click Campaign Consulting</li><li>Email Marketing</li><li>SEO Copywriting</li><li>Reputation Management</li></ul></div>
    <div class="footer-col" style="width:165px"><h3>Website Design</h3><ul><li>Web Design</li><li>E-commerce</li><li>Multimedia</li><li>Web Application Development</li></ul></div>
    <div class="footer-col" style="width:118px"><h3>IT Consulting</h3><ul><li>Web Design</li><li>E-commerce</li><li>Multimedia</li><li>Web Application</li></ul></div>
    <div class="footer-col" style="width:110px"><h3>Brellow Interactive</h3><ul><li>About Us</li><li>Our Work</li><li>Contact Us</li></ul></div>
  </div>
  <div class="footer-bottom"><span>Copyright by Brellow Interactive Group</span><span>All rights reserved</span></div>
</footer>
</body>
</html>
```